依頼概要
愛媛県愛南町特産の柑橘「河内晩柑」の果汁100%を沖縄県で「果汁(ジュース)でも割材でも飲める商品」として販売を計画しています。背景には河内晩柑は苦味と酸味のスッキリ味が特徴で甘味がありません。また沖縄は泡盛へ割る飲酒習慣があるほか、通年で暖かくサッパリ味、苦味が好まれる傾向にあるからです。6月に沖縄県で試飲会を行い手応えを得ました。

しかし、沖縄にはシークァーサーがあり、割材=シークァーサーのイメージです。そこでシークァーサーに代わる割材として河内晩柑で需要喚起、市場開拓を狙っています。
つきましては、1/28-1/29に沖縄市の市場にて「河内晩柑100%ジュースの試飲会」と「ラベルデザイン投票」を現地で行います。
当日は720mlと150mlの容器に入ったジュースを用意し、試飲後に沖縄県在住の方が(このラベル=イメージなら買いたい)というラベルデザイン案に票を投じます。

求めているのは「愛媛県愛南町、沖縄県、河内晩柑、割材でも100%果汁でもおいしく飲めるお得感」というイメージを盛り込んだラベルデザインです。容器は720mlと150mlの2種類ですが、150mlのデザインを150%拡大して720mlに流用します。なので依頼は一種類のラベルデザインです。

投票で票を最多獲得したラベルデザイン案を採用しますが、投票後に寄せられた意見を元に軽度なブラッシュアップ(例:色味、レイアウト、線種など)があることを想定しています。予めご了承ください。

愛南町河内晩柑ホームページ
https://www.sakurane-shiki.example/nousan/osusume/kajitsu/hoshizora/minorikan.html

*追加情報がある場合は加筆させていただきます。

<依頼内容>
・沖縄県で「100%果汁」でも「割材」としても販売する愛媛県愛南町河内晩柑100%果汁のラベルデザイン
・ラベルデザインサイズは150mlが「W:40mm、H:80mm」の範囲内、720mlは150mlのデザインを150%拡大します。
・複雑な形で細かい切り抜き設定が必要なラベルデザインも可能ですが、シールの形状は扱いやすい楕円や四角などのデザインが好みです。
・期待するラベルデザインは、「愛媛県愛南町、沖縄県、河内晩柑、割材でも100%ジュースでもおいしく飲めるお得感」というイメージを盛り込んだものです。コラボデザインもイメージになります。
・ラベルデザインの表記は「漢字、ひらがな、カタカナ、英語表記など」問いませんが、沖縄県の方が「欲しい」という需要の喚起ができるようお願いします。
・1/28-1/29に沖縄県沖縄市の「ゆいまわる市場」にて試飲会と試飲参加者を対象にしたラベルデザインコンテスト(投票)を行います。
・デザインの決定は1月末の予定です。
・1/28-1/29のラベルデザインコンテンスト時に投票者から色味やレイアウトなど軽度な変更を依頼された場合は修正をお願いする可能性があります。
・納品はイラストレーター形式の場合、CS6の古いバージョンでのファイルをお願いします。またPDFでも提供願います。
・ご提案いただくラベルデザイン案には創作意図などを添えていただくと幸いです。
(11/25)表現を正確にしました。
甘みが無いと表記しましたが、正確には「甘みと酸味のバランスの良いさわやかな味でほのかな苦味が特徴」です。

(11/25)写真と2点(150ml瓶、河内晩柑を切った断面)追加しました。
【追記(12/10)】
この度は、ご提案いただき、ありがとうございました。素敵なデザイン案が届き始めました。
そこで一点の再考をお願いします。
今回の依頼は「沖縄県で販売する河内晩柑100%果汁」です。ご提案いたいたデザイン案の多くはキーワードの一つである「沖縄県での販売」という訴求ポイントが欠けている気がします。
ご提案のデザインの多くは、沖縄県外でも売れる気がしますが、狙っているのは「沖縄県」です。
参考までに追記いたします。
【追記:12月31日】
この度は、愛媛県愛南町産の河内晩柑100%果汁のラベルデザインへの提案をありがとうございました。
全てのデザイン案を愛南町と精査している最中です。
そしてツクリエルさんとも協議し、1/28-1/29に沖縄県沖縄市にある「みどり南風産直センター_ゆいまわる〜市場」にて来場者による投票でデザインを決定するため、最終選定日を1/31にさせていただくことになりました。
しばらく時間を要しますが、ご容赦ください。よろしくお願いします。

この度は「愛媛県愛南町河内晩柑100%果汁」のラベルデザインへのご参加、ありがとうございました。
1/28-1/29に沖縄県沖縄市にある「ゆいまわる〜市場」にて投票を行い、計276人が参加しました。
その結果、「愛南町(愛媛県)と沖縄のイメージが上手に融合した」と評されたデザインが最多得票となりました。

大変、長らくお待たせして恐縮ですが、重ねてのご参加、ありがとうございました。
一つ一つのデザインに理由や背景があることがわかりました。
また、このような機会がありましたら、ご案内したいと思います。

```html
<!DOCTYPE html>
<html lang="ja">
<head>
<meta charset="utf-8">
<title>河内晩柑 果汁100% ラベルデザイン</title>
<link rel="stylesheet" href="https://fonts.googleapis.com/css2?family=Shippori+Mincho:wght@500;800&family=Noto+Sans+JP:wght@400;700&display=swap">
<style>
  :root {
    --paper: #ffffff;
    --ink: #1a1a1a;
    --ink-soft: #3a3a3a;
    --badge: #111111;
    --orange: #f29a1f;
    --citrus: #f6c431;
    --hibiscus: #e2466f;
    --leaf: #2f9a63;
    --wave: #3aa8d8;
    --line: #d9d9d9;
    --photo-top: #f1f1ef;
    --photo-bottom: #d8d6d0;
  }
  * { box-sizing: border-box; margin: 0; padding: 0; }
  html, body { width: 818px; height: 1200px; overflow: hidden; background: var(--paper); }
  .sheet { position: relative; width: 818px; height: 1200px; }

  .label {
    position: absolute; top: 40px; width: 275px; height: 535px;
    background: var(--paper); border: 1px solid var(--line); overflow: hidden;
  }
  .label--rect { left: 110px; }
  .label--oval { left: 435px; border-radius: 138px; }

  .label__art { position: absolute; left: 0; right: 0; }
  .label__art--top {
    top: 0; height: 92px;
    background: linear-gradient(100deg, var(--hibiscus) 0%, var(--citrus) 35%, var(--orange) 60%, var(--hibiscus) 85%, var(--wave) 100%);
    opacity: .85;
  }
  .label__art--bottom {
    bottom: 0; height: 92px;
    background: linear-gradient(80deg, var(--citrus) 0%, var(--wave) 30%, var(--hibiscus) 55%, var(--leaf) 75%, var(--orange) 100%);
    opacity: .85;
  }

  .label__badge {
    position: absolute; top: 108px; left: 28px; width: 56px; height: 56px;
    border-radius: 50%; background: var(--badge); color: var(--paper);
    display: flex; flex-direction: column; align-items: center; justify-content: center;
    font-family: "Noto Sans JP", sans-serif; font-weight: 700; line-height: 1.1;
  }
  .label__badge span:first-child { font-size: 13px; }
  .label__badge span:last-child { font-size: 12px; }

  .label__vertical { position: absolute; writing-mode: vertical-rl; color: var(--ink); }
  .label__name {
    top: 170px; left: 86px;
    font-family: "Shippori Mincho", serif; font-weight: 800; font-size: 52px; letter-spacing: 2px;
  }
  .label__origin {
    top: 108px; left: 150px;
    font-family: "Shippori Mincho", serif; font-weight: 500; font-size: 30px; letter-spacing: 1px;
  }
  .label__copy {
    top: 108px; left: 196px; height: 290px;
    font-family: "Noto Sans JP", sans-serif; font-size: 12px; line-height: 1.9; color: var(--ink-soft);
  }
  .label__volume {
    position: absolute; top: 410px; left: 30px;
    font-family: "Shippori Mincho", serif; font-weight: 500; font-size: 20px; color: var(--orange);
  }

  .bottle-photo {
    position: absolute; left: 262px; top: 655px; width: 330px; height: 480px;
    background: linear-gradient(180deg, var(--photo-top) 0%, var(--photo-bottom) 100%);
  }
</style>
</head>
<body>
<main class="sheet">

  <section class="label label--rect" aria-label="長方形ラベル">
    <div class="label__art label__art--top" role="img" aria-label="ハイビスカスと河内晩柑の輪切り、沖縄の波模様のイラスト"></div>
    <div class="label__art label__art--bottom" role="img" aria-label="河内晩柑の果実と葉、ハイビスカスのイラスト"></div>
    <div class="label__badge"><span>果汁</span><span>100%</span></div>
    <p class="label__vertical label__name">河内晩柑</p>
    <p class="label__vertical label__origin">愛媛県愛南町</p>
    <p class="label__vertical label__copy">果実のほろ苦さと甘酸っぱさが広がる<br>泡盛割りにも合う爽やかな味わい</p>
    <p class="label__volume">150ml</p>
  </section>

  <section class="label label--oval" aria-label="楕円形ラベル">
    <div class="label__art label__art--top" role="img" aria-label="ハイビスカスと河内晩柑の輪切り、沖縄の波模様のイラスト"></div>
    <div class="label__art label__art--bottom" role="img" aria-label="河内晩柑の果実と葉、ハイビスカスのイラスト"></div>
    <div class="label__badge"><span>果汁</span><span>100%</span></div>
    <p class="label__vertical label__name">河内晩柑</p>
    <p class="label__vertical label__origin">愛媛県愛南町</p>
    <p class="label__vertical label__copy">果実のほろ苦さと甘酸っぱさが広がる<br>泡盛割りにも合う爽やかな味わい</p>
    <p class="label__volume">150ml</p>
  </section>

  <div class="bottle-photo" role="img" aria-label="ラベルを貼った河内晩柑果汁150ml瓶2本の写真"></div>

</main>
</body>
</html>
```